Rebrand for a franchise company

We have a very successful business in LA and we are franchising. The franchise website is not telling the story and we are having a harder time than we thought to sell franchises. We have been told that while our websites are fine for LA and the existing business, we need to rebrand for franchise sales.
our current franchise website is: www.mirelton-quaylefranchise.org

Target Market(s)

potential franchisees in the country who want a business that enriches children's lives

Industry/Entity Type

Business

Logo Text

Fun Comes First!

Number of Pages Required

5+ page

Font styles to use
Other font styles liked:
• century gothic (?)

Requirements
Must have
• a fun, exciting, and appealing feel and brand
Nice to have
• an environment where excitement is built through color, movement, and brand
• Refer to our existing website for pix

```html
<!DOCTYPE html>
<html lang="en">
<head>
<meta charset="utf-8">
<title>Mirelton-Quayle Enrichment – Franchise Opportunities</title>
<link href="https://fonts.googleapis.com/css2?family=Courgette&family=Open+Sans:wght@400;600;700&display=swap" rel="stylesheet">
<style>
:root{
  --brown:#4a2c1d;
  --brown-dark:#3a2216;
  --nav:#b9582b;
  --orange:#e8742c;
  --orange-soft:#f2a25a;
  --green:#7dbb36;
  --blue:#2ea3d8;
  --amber:#f0a12a;
  --pink:#e2447e;
  --text:#6b5a50;
  --muted:#9a8c84;
  --white:#ffffff;
  --bg:#ffffff;
}
*{margin:0;padding:0;box-sizing:border-box}
html,body{width:845px;height:1200px;overflow:hidden}
body{background:var(--bg);font-family:"Open Sans",Arial,sans-serif;color:var(--text);font-size:9px;line-height:1.5}
.page{width:845px;height:1200px;position:relative}

/* header */
.site-header{height:78px;display:flex;align-items:center;justify-content:space-between;padding:0 36px 0 38px}
.brand{display:flex;align-items:center;gap:8px}
.brand-dot{width:26px;height:26px;border-radius:50%;background:var(--orange)}
.brand-name{font-family:"Open Sans",Arial,sans-serif;font-weight:700;font-size:17px;color:var(--brown);line-height:1;letter-spacing:.5px}
.brand-tag{font-size:8px;color:var(--muted);margin-top:4px}
.header-actions{display:flex;align-items:center;gap:10px}
.phone{display:flex;align-items:center;gap:6px;font-weight:700;font-size:15px;color:var(--brown);margin-right:8px}
.btn{font-size:8px;font-weight:700;color:var(--white);padding:5px 11px;border-radius:2px;text-transform:uppercase}
.btn-signin{background:var(--green)}
.btn-signup{background:var(--orange)}

/* nav */
.main-nav{height:28px;background:var(--nav);display:flex;padding-left:95px}
.main-nav a{color:var(--white);text-decoration:none;font-size:7.5px;font-weight:600;text-transform:uppercase;padding:0 15px;line-height:28px}
.main-nav a.active{background:var(--brown-dark)}

/* hero */
.hero{position:relative;height:344px;background:linear-gradient(120deg,#e9c7a4 0%,#d79a74 35%,#c9856a 55%,#8fb3c9 80%,#e0b08a 100%)}
.hero-title{position:absolute;left:0;right:0;top:120px;text-align:center;font-family:"Courgette",cursive;color:var(--white);font-size:50px;line-height:1.05}
.hero-arrow{position:absolute;top:158px;width:22px;height:22px;background:rgba(60,40,30,.55);display:flex;align-items:center;justify-content:center}
.hero-arrow.prev{left:12px}
.hero-arrow.next{right:12px}

/* welcome */
.welcome{text-align:center;padding:24px 110px 0}
.welcome h1{font-family:"Courgette",cursive;font-weight:400;color:var(--orange);font-size:21px}
.welcome h2{font-family:"Courgette",cursive;font-weight:400;color:var(--brown);font-size:16px;margin-top:2px}
.welcome p{font-size:8px;color:var(--muted);margin-top:10px;line-height:1.7}

/* programs */
.programs{display:flex;gap:11px;padding:0 38px;margin-top:22px}
.program{flex:1}
.program-photo{height:94px}
.program-body{height:126px;padding:16px 14px;text-align:center;color:var(--white)}
.program-body h3{font-family:"Courgette",cursive;font-weight:400;font-size:15px;line-height:1.2}
.program-body p{font-size:7.5px;margin-top:6px;opacity:.95}
.green{background:var(--green)}
.blue{background:var(--blue)}
.amber{background:var(--amber)}
.pink{background:var(--pink)}

/* news */
.news{display:flex;gap:40px;padding:0 38px;margin-top:38px}
.news h4{font-family:"Courgette",cursive;font-weight:400;color:var(--brown);font-size:20px;margin-bottom:14px}
.events{width:255px}
.event{display:flex;gap:12px;margin-bottom:20px}
.event-date{width:34px;flex:none;text-align:center}
.event-date .day{background:var(--orange);color:var(--white);font-weight:700;font-size:11px;padding:4px 0}
.event-date .mon{background:#f1e8e2;color:var(--brown);font-size:7.5px;padding:2px 0}
.event-date.alt .day{background:var(--green)}
.event h5{font-family:"Courgette",cursive;font-weight:400;color:var(--orange);font-size:13px}
.event p{font-size:7.5px;color:var(--muted)}
.blog{flex:1}
.blog-grid{display:flex;gap:16px}
.blog-photo{width:176px;height:160px}
.blog-list{flex:1}
.blog-item{display:flex;gap:10px;margin-bottom:14px}
.blog-thumb{width:40px;height:40px;flex:none}
.blog-item .date{font-size:7.5px;color:var(--orange);font-weight:700}
.blog-item p{font-size:7.5px;color:var(--muted)}

/* footer */
.site-footer{position:absolute;left:0;right:0;bottom:0;height:72px;background:var(--brown);display:flex;align-items:center;padding:0 38px;color:#c9b6a8;font-size:7.5px}
.footer-copy{width:255px}
.footer-contact{flex:1;padding-left:40px}
.social{display:flex;gap:12px}
.social span{width:18px;height:18px;border-radius:50%;background:#6a4a38}
</style>
</head>
<body>
<div class="page">

  <header class="site-header">
    <div class="brand">
      <span class="brand-dot"></span>
      <div>
        <div class="brand-name">MIRELTON-QUAYLE ENRICHMENT</div>
        <div class="brand-tag">Educational Services for Young People</div>
      </div>
    </div>
    <div class="header-actions">
      <div class="phone">
        <svg width="14" height="14" viewBox="0 0 24 24"><path fill="#e8742c" d="M6.6 10.8a15.1 15.1 0 0 0 6.6 6.6l2.2-2.2c.3-.3.7-.4 1-.2 1.1.4 2.3.6 3.6.6.6 0 1 .4 1 1V20c0 .6-.4 1-1 1A17 17 0 0 1 3 4c0-.6.4-1 1-1h3.5c.6 0 1 .4 1 1 0 1.3.2 2.5.6 3.6.1.3 0 .7-.2 1z"/></svg>
        (555) 214-0387
      </div>
      <span class="btn btn-signin">Sign In</span>
      <span class="btn btn-signup">Sign Up</span>
    </div>
  </header>

  <nav class="main-nav">
    <a class="active">Home</a>
    <a>FAQ</a>
    <a>Why Enrichment</a>
    <a>Sign Up for Free</a>
    <a>Franchise Opportunities</a>
    <a>Contact Us</a>
    <a>Franchise Login</a>
  </nav>

  <section class="hero" role="img" aria-label="Smiling children learning together in a classroom">
    <div class="hero-title">Franchise<br>Opportunities</div>
    <span class="hero-arrow prev"><svg width="8" height="10" viewBox="0 0 8 10"><path d="M6 1 2 5l4 4" stroke="#fff" stroke-width="2" fill="none"/></svg></span>
    <span class="hero-arrow next"><svg width="8" height="10" viewBox="0 0 8 10"><path d="m2 1 4 4-4 4" stroke="#fff" stroke-width="2" fill="none"/></svg></span>
  </section>

  <section class="welcome">
    <h1>Welcome to Mirelton-Quayle Enrichment!</h1>
    <h2>Exciting programs ... at school ... after school</h2>
    <p>At Mirelton-Quayle Enrichment, we bring hands-on learning to schools across the country. Our after-school classes, camps and parties spark curiosity, build confidence and help young people discover what they love. As a franchise owner you join a proven program, a caring team and a growing network of families who trust us with their children every single week.</p>
  </section>

  <section class="programs">
    <article class="program">
      <div class="program-photo" role="img" aria-label="Children playing outdoors at school" style="background:linear-gradient(135deg,#9fcf6a,#5f9bd0)"></div>
      <div class="program-body green"><h3>School Enrichment Programs</h3><p>Fun science, art and sports classes held right on campus.</p></div>
    </article>
    <article class="program">
      <div class="program-photo" role="img" aria-label="Kids at a tournament table" style="background:linear-gradient(135deg,#7cc0e4,#d9a27a)"></div>
      <div class="program-body blue"><h3>Tournaments</h3><p>Friendly chess and game tournaments for every skill level.</p></div>
    </article>
    <article class="program">
      <div class="program-photo" role="img" aria-label="Children doing crafts at summer camp" style="background:linear-gradient(135deg,#f3c27a,#c98a6b)"></div>
      <div class="program-body amber"><h3>Summer Camps &amp; Activities</h3><p>Week-long camps full of crafts, games and new friends.</p></div>
    </article>
    <article class="program">
      <div class="program-photo" role="img" aria-label="Kids celebrating at a birthday party" style="background:linear-gradient(135deg,#f1a3b8,#d78c72)"></div>
      <div class="program-body pink"><h3>Birthday Parties</h3><p>Themed parties with activities that kids will remember.</p></div>
    </article>
  </section>

  <section class="news">
    <div class="events">
      <h4>Up Comming Events</h4>
      <div class="event">
        <div class="event-date"><div class="day">26</div><div class="mon">Mar</div></div>
        <div><h5>News Headline Here</h5><p>Join us for an open house and learn how our programs work.</p></div>
      </div>
      <div class="event">
        <div class="event-date alt"><div class="day">18</div><div class="mon">Apr</div></div>
        <div><h5>News Headline Here</h5><p>Join us for an open house and learn how our programs work.</p></div>
      </div>
    </div>
    <div class="blog">
      <h4>Blog News</h4>
      <div class="blog-grid">
        <div class="blog-photo" role="img" aria-label="Group of children smiling together" style="background:linear-gradient(135deg,#e7b38c,#7fb0d2)"></div>
        <div class="blog-list">
          <div class="blog-item">
            <div class="blog-thumb" role="img" aria-label="Child drawing" style="background:linear-gradient(135deg,#f0c08e,#c48768)"></div>
            <div><div class="date">April 30 2015</div><p>Short post title about our latest class</p></div>
          </div>
          <div class="blog-item">
            <div class="blog-thumb" role="img" aria-label="Kids in a classroom" style="background:linear-gradient(135deg,#9cc6e0,#d6a07c)"></div>
            <div><div class="date">April 30 2015</div><p>Short post title about our latest class</p></div>
          </div>
          <div class="blog-item">
            <div class="blog-thumb" role="img" aria-label="Children playing a game" style="background:linear-gradient(135deg,#b5d78a,#d89b78)"></div>
            <div><div class="date">April 30 2015</div><p>Short post title about our latest class</p></div>
          </div>
        </div>
      </div>
    </div>
  </section>

  <footer class="site-footer">
    <div class="footer-copy">Copyright © 2015 Mirelton-Quayle Enrichment<br>Privacy Policy | Terms of Use</div>
    <div class="footer-contact">Email: franchise@mirelton-quayle.org<br>Phone: (555) 214-0387</div>
    <div class="social"><span></span><span></span><span></span><span></span></div>
  </footer>

</div>
</body>
</html>
```